QLB Insurance Services Business Card
Slogan - Quiet Lanterns Burn
Creative Brief
Use specific fonts
Feel free to use the same font as used in my logo OR whatever looks good
Simple
Marisol (Greta) Dovik
Broker
20387 Marlowpine Dr. Tustin, CA 92740
greta@qlbinsurance.example
www.qblinsurance.example
0K47382
*Commercial Liability *Commercial Property *Business Owner Policy *Excess/Umbrella Liability *Worker's Compensation *Professional Liability *Commercial/Business Auto *Homeowner/Auto Insurance *Flood/Earthquake Insurance and more *Specializing import/export and manufacture company

```html
<!DOCTYPE html>
<html lang="en">
<head>
<meta charset="utf-8">
<title>QLB Insurance Services — Stationery Set</title>
<link href="https://fonts.googleapis.com/css2?family=Open+Sans:wght@400;600;700&display=swap" rel="stylesheet">
<style>
  :root {
    --stage: #1e1f22;
    --paper: #ffffff;
    --blue-deep: #0b4ea2;
    --blue-mid: #1f7fd6;
    --blue-light: #8cc8f2;
    --ink: #3a3f47;
    --ink-soft: #8a9099;
    --rule: #c9ced6;
    --ghost: #eceef1;
  }
  * { box-sizing: border-box; margin: 0; padding: 0; }
  html, body { width: 1200px; height: 574px; overflow: hidden; }
  body {
    background: var(--stage);
    font-family: "Open Sans", Arial, sans-serif;
    color: var(--ink);
    position: relative;
  }
  .piece { position: absolute; background: var(--paper); overflow: hidden; box-shadow: 0 4px 14px rgba(0,0,0,.45); }
  .edge-bar {
    position: absolute; top: 0; bottom: 0;
    background: linear-gradient(to bottom, var(--blue-deep), var(--blue-mid) 55%, var(--blue-light));
  }
  .brand { position: absolute; display: flex; align-items: center; gap: 6px; }
  .brand-dot { width: 10px; height: 10px; border-radius: 50%; background: var(--blue-mid); }
  .brand-name { font-weight: 700; color: var(--blue-deep); letter-spacing: .04em; white-space: nowrap; }
  .ghost-mark {
    position: absolute; font-weight: 700; color: var(--ghost);
    letter-spacing: .02em; line-height: 1; white-space: nowrap;
  }
  .fine { font-size: 5px; color: var(--ink-soft); line-height: 1.6; white-space: nowrap; }

  /* Letterhead */
  .letterhead { left: 36px; top: 72px; width: 324px; height: 485px; }
  .letterhead .edge-bar { left: 10px; width: 9px; }
  .letterhead .brand { left: 30px; top: 14px; }
  .letterhead .brand-name { font-size: 8px; }
  .letterhead .ghost-mark { left: 44px; top: 200px; font-size: 150px; }
  .letter-footer { position: absolute; left: 30px; right: 16px; bottom: 12px; display: flex; justify-content: space-between; align-items: flex-end; }

  /* Fax */
  .fax { left: 384px; top: 72px; width: 324px; height: 485px; }
  .fax .edge-bar { left: 10px; width: 9px; }
  .fax .brand { left: 0; right: 0; top: 14px; justify-content: center; }
  .fax .brand-name { font-size: 8px; }
  .fax-title { position: absolute; left: 30px; top: 88px; font-size: 22px; font-weight: 400; color: var(--ink); letter-spacing: .04em; }
  .fax-fields { position: absolute; left: 30px; right: 22px; top: 120px; display: grid; grid-template-columns: 1fr 1fr; column-gap: 16px; row-gap: 9px; }
  .fax-field { font-size: 5.5px; color: var(--ink-soft); border-bottom: 1px solid var(--rule); padding-bottom: 2px; }
  .fax-rule { position: absolute; left: 30px; right: 22px; height: 2px; background: var(--ink); }
  .fax-checks { position: absolute; left: 30px; right: 22px; top: 218px; display: flex; justify-content: space-between; }
  .fax-check { display: flex; align-items: center; gap: 3px; font-size: 5.5px; color: var(--ink-soft); }
  .fax-check::before { content: ""; width: 6px; height: 6px; border: 1px solid var(--ink-soft); }
  .fax .letter-footer { left: 30px; }

  /* Envelopes */
  .envelope { left: 763px; width: 410px; height: 138px; }
  .env-back-open { top: 48px; background: transparent; box-shadow: none; overflow: visible; }
  .env-back-open svg { position: absolute; inset: 0; }
  .env-back-open .brand { left: 0; right: 0; top: 66px; justify-content: center; }
  .env-back-open .brand-name { font-size: 14px; color: var(--paper); }
  .env-back-open .brand-dot { background: var(--paper); }
  .env-back-closed { top: 126px; }
  .env-back-closed svg { position: absolute; inset: 0; }
  .env-back-closed .brand { left: 0; right: 0; top: 60px; justify-content: center; }
  .env-back-closed .brand-name { font-size: 12px; }
  .env-front { top: 214px; height: 164px; }
  .env-front .edge-bar { left: 12px; width: 8px; }
  .env-front .brand { left: 30px; top: 26px; }
  .env-front .brand-name { font-size: 8px; }
  .env-front .fine { position: absolute; left: 30px; top: 42px; }
  .env-front .ghost-mark { right: 22px; top: 40px; font-size: 92px; }

  /* Business cards */
  .card { width: 122px; height: 68px; }
  .card-front-a { left: 806px; top: 392px; }
  .card-front-a .edge-bar { left: 6px; width: 5px; }
  .card-front-a .brand { left: 16px; top: 8px; }
  .card-front-a .brand-name { font-size: 5.5px; }
  .card-front-a .brand-dot { width: 5px; height: 5px; }
  .card-front-a .fine { position: absolute; left: 16px; bottom: 6px; font-size: 3.6px; }
  .card-front-b { left: 950px; top: 392px; }
  .card-front-b .brand { left: 0; right: 0; top: 8px; justify-content: center; }
  .card-front-b .brand-name { font-size: 6px; }
  .card-front-b .brand-dot { width: 5px; height: 5px; }
  .card-person { position: absolute; right: 10px; top: 34px; text-align: right; }
  .card-person-name { font-size: 4.6px; font-weight: 700; color: var(--ink); white-space: nowrap; }
  .card-person-role { font-size: 3.8px; color: var(--ink-soft); }
  .card-front-b .fine { position: absolute; left: 8px; bottom: 5px; font-size: 3.6px; }
  .card-services { left: 806px; top: 470px; padding: 8px 7px; }
  .card-services .brand { position: static; justify-content: center; margin-bottom: 4px; }
  .card-services .brand-name { font-size: 5px; }
  .card-services .brand-dot { width: 4px; height: 4px; }
  .service-list { font-size: 3.2px; color: var(--ink-soft); line-height: 1.55; text-align: center; }
  .card-back { left: 950px; top: 470px; background: linear-gradient(135deg, var(--blue-deep), var(--blue-mid)); }
  .card-back .brand { left: 0; right: 0; top: 22px; flex-direction: column; gap: 3px; }
  .card-back .brand-name { color: var(--paper); font-size: 9px; }
  .card-back .brand-dot { background: var(--paper); width: 6px; height: 6px; }
  .card-back .tagline { font-size: 4px; color: var(--blue-light); letter-spacing: .08em; }
</style>
</head>
<body>

  <!-- Letterhead -->
  <section class="piece letterhead">
    <div class="edge-bar"></div>
    <div class="brand"><span class="brand-dot"></span><span class="brand-name">QLB Insurance Services</span></div>
    <div class="ghost-mark" aria-hidden="true">QLB</div>
    <div class="letter-footer">
      <div class="fine">20387 Marlowpine Dr.<br>Tustin, CA 92740</div>
      <div class="fine">T (714) 555-0142<br>F (714) 555-0187</div>
      <div class="fine">greta@qlbinsurance.example<br>www.qblinsurance.example</div>
      <div class="fine">License No. 0K47382</div>
    </div>
  </section>

  <!-- Fax cover -->
  <section class="piece fax">
    <div class="edge-bar"></div>
    <div class="brand"><span class="brand-dot"></span><span class="brand-name">QLB Insurance Services</span></div>
    <h1 class="fax-title">FAX</h1>
    <div class="fax-fields">
      <div class="fax-field">To:</div><div class="fax-field">From:</div>
      <div class="fax-field">Fax:</div><div class="fax-field">Pages:</div>
      <div class="fax-field">Phone:</div><div class="fax-field">Date:</div>
      <div class="fax-field">Re:</div><div class="fax-field">CC:</div>
    </div>
    <div class="fax-rule" style="top:206px"></div>
    <div class="fax-checks">
      <span class="fax-check">Urgent</span>
      <span class="fax-check">For Review</span>
      <span class="fax-check">Please Comment</span>
      <span class="fax-check">Please Reply</span>
      <span class="fax-check">Please Recycle</span>
    </div>
    <div class="fax-rule" style="top:234px"></div>
    <div class="letter-footer">
      <div class="fine">20387 Marlowpine Dr.<br>Tustin, CA 92740</div>
      <div class="fine">T (714) 555-0142<br>F (714) 555-0187</div>
      <div class="fine">greta@qlbinsurance.example<br>www.qblinsurance.example</div>
      <div class="fine">License No. 0K47382</div>
    </div>
  </section>

  <!-- Envelope, back with open flap -->
  <section class="piece envelope env-back-open">
    <svg width="410" height="138" viewBox="0 0 410 138" aria-hidden="true">
      <defs>
        <linearGradient id="flap" x1="0" y1="0" x2="0" y2="1">
          <stop offset="0" stop-color="#0b4ea2"/>
          <stop offset="1" stop-color="#4aa3ea"/>
        </linearGradient>
      </defs>
      <rect x="0" y="0" width="410" height="138" fill="#ffffff"/>
      <rect x="0" y="0" width="410" height="138" fill="url(#flap)"/>
      <path d="M0 138 L205 70 L410 138 Z" fill="#ffffff" opacity=".9"/>
    </svg>
    <div class="brand"><span class="brand-dot"></span><span class="brand-name">QLB</span></div>
  </section>

  <!-- Envelope, back with closed flap -->
  <section class="piece envelope env-back-closed">
    <svg width="410" height="138" viewBox="0 0 410 138" aria-hidden="true">
      <path d="M0 0 L205 82 L410 0" fill="none" stroke="#c9ced6" stroke-width="1.2"/>
      <path d="M0 138 L170 70 M410 138 L240 70" fill="none" stroke="#e1e4e9" stroke-width="1"/>
    </svg>
    <div class="brand"><span class="brand-dot"></span><span class="brand-name">QLB</span></div>
  </section>

  <!-- Envelope, front -->
  <section class="piece envelope env-front">
    <div class="edge-bar"></div>
    <div class="brand"><span class="brand-dot"></span><span class="brand-name">QLB Insurance Services</span></div>
    <div class="fine">20387 Marlowpine Dr. Tustin, CA 92740</div>
    <div class="ghost-mark" aria-hidden="true">QLB</div>
  </section>

  <!-- Business card, front with bar -->
  <section class="piece card card-front-a">
    <div class="edge-bar"></div>
    <div class="brand"><span class="brand-dot"></span><span class="brand-name">QLB Insurance Services</span></div>
    <div class="fine">greta@qlbinsurance.example</div>
  </section>

  <!-- Business card, front with name -->
  <section class="piece card card-front-b">
    <div class="brand"><span class="brand-dot"></span><span class="brand-name">QLB Insurance Services</span></div>
    <div class="card-person">
      <div class="card-person-name">Marisol (Greta) Dovik</div>
      <div class="card-person-role">Broker · Lic. 0K47382</div>
    </div>
    <div class="fine">T (714) 555-0142 · greta@qlbinsurance.example<br>20387 Marlowpine Dr. Tustin, CA 92740</div>
  </section>

  <!-- Business card, services -->
  <section class="piece card card-services">
    <div class="brand"><span class="brand-dot"></span><span class="brand-name">QLB Insurance Services</span></div>
    <p class="service-list">
      Commercial Liability · Commercial Property · Business Owner Policy<br>
      Excess/Umbrella Liability · Worker's Compensation · Professional Liability<br>
      Commercial/Business Auto · Homeowner/Auto Insurance<br>
      Flood/Earthquake Insurance and more<br>
      Specializing import/export and manufacture company<br>
      www.qblinsurance.example
    </p>
  </section>

  <!-- Business card, blue back -->
  <section class="piece card card-back">
    <div class="brand">
      <span class="brand-dot"></span>
      <span class="brand-name">QLB</span>
      <span class="tagline">Quiet Lanterns Burn</span>
    </div>
  </section>

</body>
</html>
```